I have a Moulding business and I’m looking to hire experienced finish carpenters to install all types of doors trim. Please provide me with a advertising poster in English.
I am looking for a poster to advertise the job openings thanks

```html
<!DOCTYPE html>
<html lang="en">
<head>
<meta charset="utf-8">
<title>We Are Hiring – Finish Carpenters</title>
<link rel="stylesheet" href="https://fonts.googleapis.com/css2?family=Montserrat:wght@400;500;700;800&display=swap">
<style>
  :root {
    --backdrop: #e4e4e4;
    --wood-light: #d99a55;
    --wood-mid: #c47f3c;
    --wood-dark: #a9662a;
    --teal: #4e9690;
    --teal-text: #3f8a84;
    --ink: #2b2622;
    --white: #ffffff;
    --string: #3a2a22;
  }
  * { margin: 0; padding: 0; box-sizing: border-box; }
  html, body {
    width: 1040px;
    height: 1200px;
    overflow: hidden;
    background: var(--backdrop);
    font-family: "Montserrat", sans-serif;
  }
  .poster {
    position: absolute;
    left: 90px;
    top: 20px;
    width: 860px;
    height: 1160px;
    overflow: hidden;
    background: linear-gradient(160deg, var(--wood-light) 0%, var(--wood-mid) 55%, var(--wood-dark) 100%);
  }
  .hanger { position: absolute; left: 0; top: 0; }
  .hiring-sign {
    position: absolute;
    left: 35px;
    top: 185px;
    width: 500px;
    height: 316px;
    background: var(--teal);
    border: 9px solid var(--white);
    transform: rotate(13.8deg);
    display: flex;
    align-items: center;
    justify-content: center;
    text-align: center;
    color: var(--white);
    font-weight: 800;
    font-size: 76px;
    line-height: 1.05;
    letter-spacing: 1px;
  }
  .contact {
    position: absolute;
    right: 46px;
    top: 36px;
    text-align: right;
  }
  .contact-lead { font-size: 43px; font-weight: 500; color: var(--ink); line-height: 1.1; }
  .contact-email { font-size: 28px; font-weight: 700; color: var(--teal-text); margin-top: 8px; }
  .contact-question { font-size: 29px; font-weight: 500; color: var(--ink); margin-top: 18px; letter-spacing: 1px; }
  .contact-phone { font-size: 28px; font-weight: 700; color: var(--teal-text); margin-top: 12px; letter-spacing: 1px; }
  .job-copy {
    position: absolute;
    left: 54px;
    top: 570px;
    color: var(--white);
    text-transform: uppercase;
    line-height: 1;
  }
  .job-copy span { display: block; }
  .line-we-are { font-size: 62px; font-weight: 500; }
  .line-looking { font-size: 42px; font-weight: 500; margin-top: 14px; }
  .line-hire { font-size: 98px; font-weight: 500; margin-top: 8px; }
  .line-experienced { font-size: 50px; font-weight: 500; margin-top: 6px; }
  .line-finish { font-size: 50px; font-weight: 800; letter-spacing: 9px; margin-top: 8px; }
  .line-carpenters { font-size: 46px; font-weight: 500; letter-spacing: 1px; margin-top: 10px; }
  .line-install { font-size: 46px; font-weight: 500; margin-top: 12px; }
  .line-types { font-size: 42px; font-weight: 500; letter-spacing: 10px; margin-top: 12px; }
  .line-doors { font-size: 46px; font-weight: 800; letter-spacing: 2px; margin-top: 12px; }
  .carpenter-illustration {
    position: absolute;
    left: 505px;
    top: 400px;
    width: 335px;
    height: 730px;
    border-radius: 40px;
    background: linear-gradient(180deg, #d9b15a 0%, #c9a27a 35%, #8aa6c8 70%, #c49a6c 100%);
    opacity: 0.85;
  }
</style>
</head>
<body>
  <main class="poster">
    <svg class="hanger" width="860" height="300" aria-hidden="true">
      <line x1="321" y1="27" x2="150" y2="142" stroke="var(--string)" stroke-width="3"/>
      <line x1="321" y1="27" x2="465" y2="225" stroke="var(--string)" stroke-width="3"/>
      <circle cx="321" cy="27" r="11" fill="var(--string)"/>
    </svg>

    <div class="hiring-sign">WE ARE<br>HIRING</div>

    <div class="contact">
      <p class="contact-lead">or email us at</p>
      <p class="contact-email">hiring@oaklinetrim.com</p>
      <p class="contact-question">GOT THE SKILLS ?</p>
      <p class="contact-phone">CALL 0555-014-272</p>
    </div>

    <h1 class="job-copy">
      <span class="line-we-are">We are</span>
      <span class="line-looking">Looking to</span>
      <span class="line-hire">Hire</span>
      <span class="line-experienced">Experienced</span>
      <span class="line-finish">Finish</span>
      <span class="line-carpenters">Carpenters</span>
      <span class="line-install">To install all</span>
      <span class="line-types">Types of</span>
      <span class="line-doors">Doors trim</span>
    </h1>

    <div class="carpenter-illustration" role="img" aria-label="Cartoon carpenter in a yellow hard hat and tool belt carrying a large mallet on his shoulder"></div>
  </main>
</body>
</html>
```